Air Conditioning Advertisement

I am looking to design an ad for my HVAC company. The name of my company is Pine Hollow Cooling INC. We provide 24/7 emergency service.
Image- Ductless air conditioning unit & central air conditioning unit
Website- www.brisktundrahvac.example
company phone number- 516-387-5924

I would like an ad advertising our spring special. The spring special is $750 off a new Central Air conditioning or ductlesss air conditioning installation.

Our other special is $100 Central AC Tune up.

I attached my logo.

Target Market(s)

Home owners & small businesses

Industry/Entity Type

Air conditioning, Refrigeration & Heating

Colors
0054AA
0677BA
7BADD7
CADEEF
E8F1F8
EE7325
F08F49
F5BC92
FAE3D3
FDF4ED

Requirements
Must have
• Pictures of ductless air conditioning and central air conditioning unit.
Nice to have
• Id like to have an ad that incorporates my company colors & logos. I want this ad to stand out & show what we are offering. The ad should display, briefly say the importance of comfort in your home.

```html
<!DOCTYPE html>
<html lang="en">
<head>
<meta charset="utf-8">
<title>Pine Hollow Cooling INC — Spring Special</title>
<link rel="stylesheet" href="https://fonts.googleapis.com/css2?family=Bebas+Neue&family=Montserrat:wght@600;700;800&display=swap">
<style>
  :root {
    --navy: #0a1f5e;
    --navy-deep: #061543;
    --brand-blue: #0054AA;
    --bright-blue: #0a4fc8;
    --sky: #7BADD7;
    --orange: #EE7325;
    --white: #ffffff;
    --ink: #1c2440;
  }
  * { margin: 0; padding: 0; box-sizing: border-box; }
  html, body { width: 1200px; height: 1200px; overflow: hidden; background: var(--navy); }
  .ad {
    position: relative;
    width: 1200px;
    height: 1200px;
    overflow: hidden;
    font-family: "Montserrat", sans-serif;
    color: var(--white);
  }
  .backdrop {
    position: absolute; inset: 0;
    background:
      linear-gradient(90deg, rgba(10,40,120,0.92) 0%, rgba(12,45,130,0.75) 45%, rgba(8,30,95,0.95) 100%),
      linear-gradient(180deg, #1a3c8f 0%, #123077 60%, #0b2366 100%);
  }
  .shapes { position: absolute; inset: 0; }
  .brand-panel {
    position: absolute; left: 0; top: 0; width: 420px; height: 172px;
    background: var(--white);
    clip-path: polygon(0 0, 100% 0, 93% 100%, 0 100%);
  }
  .brand {
    position: absolute; left: 48px; top: 54px;
    display: flex; align-items: center; gap: 14px;
  }
  .brand-dot { width: 26px; height: 26px; border-radius: 50%; background: var(--orange); flex: none; }
  .brand-name {
    font-family: "Montserrat", sans-serif; font-weight: 800;
    font-size: 29px; line-height: 1.05; color: var(--brand-blue);
    width: 300px;
  }
  .brand-tagline {
    position: absolute; left: 48px; top: 156px;
    font-size: 11px; font-weight: 600; letter-spacing: 1.4px; color: var(--ink);
  }
  .headline {
    position: absolute; left: 34px; top: 258px;
    font-family: "Bebas Neue", sans-serif;
    font-size: 212px; line-height: 188px; letter-spacing: 2px;
  }
  .offers {
    position: absolute; left: 42px; top: 668px; list-style: none;
    font-family: "Bebas Neue", sans-serif; font-size: 37px; line-height: 57px; letter-spacing: 1.5px;
  }
  .offers li { position: relative; padding-left: 32px; }
  .offers li.dot::before {
    content: ""; position: absolute; left: 2px; top: 21px;
    width: 14px; height: 14px; border-radius: 50%; background: var(--orange);
  }
  .price-badge {
    position: absolute; left: 600px; top: 768px; width: 254px;
    text-align: center; font-family: "Bebas Neue", sans-serif;
  }
  .price-badge .label { font-size: 50px; line-height: 52px; letter-spacing: 0.5px; }
  .price-badge .amount { font-size: 80px; line-height: 80px; }
  .book-btn {
    position: absolute; left: 42px; top: 994px; width: 226px; height: 61px;
    background: var(--orange); border-radius: 4px;
    display: flex; align-items: center; justify-content: center;
    font-weight: 800; font-size: 20px; letter-spacing: 0.5px;
  }
  .phone {
    position: absolute; left: 42px; top: 1074px;
    font-weight: 800; font-size: 48px; letter-spacing: -0.5px;
  }
  .website {
    position: absolute; left: 44px; top: 1135px;
    font-weight: 600; font-size: 20px; letter-spacing: 4px;
  }
</style>
</head>
<body>
<main class="ad">
  <div class="backdrop" role="img" aria-label="Outdoor central air conditioning condenser units in deep blue tones"></div>

  <svg class="shapes" width="1200" height="1200" viewBox="0 0 1200 1200" aria-hidden="false">
    <g fill="#EE7325">
      <polygon points="590,0 745,0 985,240 905,320"/>
      <polygon points="1130,70 1200,0 1200,140"/>
      <polygon points="975,690 1070,600 1200,730 1200,920"/>
    </g>
    <g stroke="#ffffff" stroke-width="2" fill="none" opacity="0.9">
      <line x1="418" y1="30" x2="815" y2="262"/>
      <line x1="560" y1="0" x2="900" y2="300"/>
      <line x1="1060" y1="595" x2="1200" y2="455"/>
    </g>
    <polygon points="1130,85 1350,305 1130,525 910,305" fill="#7BADD7" stroke="#ffffff" stroke-width="8" role="img" aria-label="Technician testing an outdoor central AC unit with gauges"/>
    <polygon points="830,275 1095,540 830,805 565,540" fill="#6f88b3" stroke="#ffffff" stroke-width="8" role="img" aria-label="Technician in hard hat servicing a ductless wall-mounted air conditioner"/>
    <polygon points="975,735 1185,945 975,1155 765,945" fill="#CADEEF" stroke="#ffffff" stroke-width="8" role="img" aria-label="Hands adjusting the dials of a heating unit control panel"/>
    <polygon points="727,653 894,820 727,987 560,820" fill="#0a4fc8"/>
  </svg>

  <div class="brand-panel"></div>
  <div class="brand">
    <span class="brand-dot"></span>
    <span class="brand-name">Pine Hollow Cooling INC</span>
  </div>
  <div class="brand-tagline">AIR CONDITIONING - REFRIGERATION - HEATING</div>

  <h1 class="headline">Spring<br>Special</h1>

  <ul class="offers">
    <li class="dot">New central air conditioning</li>
    <li class="dot">&nbsp;or ductlesss air</li>
    <li>conditioning installation</li>
    <li class="dot">Our other special is $100</li>
    <li>central AC tune up.</li>
  </ul>

  <div class="price-badge">
    <div class="label">Spring Special</div>
    <div class="amount">$750</div>
  </div>

  <div class="book-btn">BOOK NOW</div>
  <div class="phone">516-387-5924</div>
  <div class="website">WWW.BRISKTUNDRAHVAC.EXAMPLE</div>
</main>
</body>
</html>
```